Zielgruppe
Planung und Realisierung von individuellen und wertbeständigen Kamin- und Ofenlösungen, sowie Fliesen- und Baddesign.
Aufgabenstellung
Wir benötigen ein möglichst schlichtes Design für Visitenkarten, bzw. Briefpapier. Für die Visitenkarten gerne auch Vorschläge mit Prägung, Ausstanzung oder mit Heißfolie. Auch Klappkarten wären denkbar. Das Design soll "das gewisse Etwas haben" und nicht zu verspielt sein.
Die Visitenkarten sind für die Firma KARMU, das Logo von der Ausstellung "talgrund" soll dezent mit eingebunden werden (bei dem Briefpapier z.B. in der Fußzeile". Die farbliche Gestaltung sollte sich an den Farben des Logos orientieren.
Schriftart für Texte: Century Gothic
Schriftfarbe: RAL 7016
Nur eine Idee: Ich könnte mir auch gut vorstellen, dass die Visitenkarte aus einer Zündholzverpackung (wenn dann aber eine besondere mit nur einem Zündholz oder einem besonders breiten) besteht: http://lindoraversand.de/produkte_briefchen.php

```html
<!DOCTYPE html>
<html lang="de">
<head>
<meta charset="utf-8">
<title>KARMU – Visitenkarte</title>
<link href="https://fonts.googleapis.com/css2?family=Questrial&display=swap" rel="stylesheet">
<style>
  :root {
    --page: #d9d9d7;
    --anthracite: #1f2a2f;
    --card-light: #e8e8e6;
    --text-dark: #383e42;
    --text-grey: #6b6f72;
    --logo-light: #e4e4e2;
    --accent: #d9801c;
    --muted: #8a9296;
  }
  * { box-sizing: border-box; margin: 0; padding: 0; }
  html, body { width: 1200px; height: 840px; overflow: hidden; }
  body {
    background: var(--page);
    font-family: "Questrial", "Century Gothic", sans-serif;
    display: flex;
    align-items: center;
    justify-content: center;
    gap: 40px;
  }
  .card {
    position: relative;
    width: 540px;
    height: 350px;
    border-radius: 3px;
    box-shadow: 0 6px 18px rgba(0,0,0,0.18);
  }

  /* Front */
  .card--front { background: var(--anthracite); color: var(--logo-light); }
  .front-brand {
    position: absolute;
    left: 0; right: 0; top: 98px;
    text-align: center;
  }
  .brand-name {
    display: inline-flex;
    align-items: center;
    gap: 14px;
    font-size: 92px;
    letter-spacing: 6px;
    line-height: 1;
  }
  .brand-dot {
    width: 16px; height: 16px;
    background: var(--accent);
    flex: none;
  }
  .brand-tagline {
    margin-top: 8px;
    font-size: 26px;
    letter-spacing: 1.5px;
  }
  .showroom {
    position: absolute;
    right: 26px; bottom: 20px;
    font-size: 17px;
    color: var(--muted);
    letter-spacing: 1px;
  }

  /* Back */
  .card--back { background: var(--card-light); color: var(--text-dark); }
  .back-brand { position: absolute; left: 40px; top: 34px; }
  .back-brand .brand-name { font-size: 52px; letter-spacing: 3px; gap: 9px; color: var(--text-dark); }
  .back-brand .brand-dot { width: 10px; height: 10px; }
  .back-brand .brand-tagline { font-size: 15px; margin-top: 4px; letter-spacing: 1px; }
  .divider {
    position: absolute;
    left: 40px; right: 48px; top: 148px;
    height: 2px;
    background: var(--anthracite);
  }
  .person {
    position: absolute;
    right: 48px; top: 110px;
    text-align: right;
  }
  .person-name { font-size: 28px; line-height: 1; }
  .person-role { margin-top: 14px; font-size: 17px; color: var(--text-grey); }
  .address {
    position: absolute;
    left: 40px; bottom: 46px;
    display: flex; gap: 10px;
    font-size: 16px; line-height: 1.35;
    color: var(--text-grey);
  }
  .contact {
    position: absolute;
    right: 40px; bottom: 34px;
    list-style: none;
    font-size: 17px;
    color: var(--text-grey);
  }
  .contact li {
    display: flex; align-items: center; justify-content: flex-end;
    gap: 12px; height: 28px;
  }
  .icon { width: 18px; height: 18px; fill: none; stroke: var(--text-dark); stroke-width: 1.6; }
  .icon--solid { fill: var(--text-dark); stroke: none; }
</style>
</head>
<body>

<section class="card card--front" aria-label="Vorderseite">
  <div class="front-brand">
    <div class="brand-name">KARMU<span class="brand-dot"></span></div>
    <p class="brand-tagline">kamine · öfen · fliesen</p>
  </div>
  <p class="showroom">talgrund</p>
</section>

<section class="card card--back" aria-label="Rückseite">
  <div class="back-brand">
    <div class="brand-name">KARMU<span class="brand-dot"></span></div>
    <p class="brand-tagline">kamine · öfen · fliesen</p>
  </div>

  <div class="person">
    <p class="person-name">Jonas Behrend</p>
    <p class="person-role">Geschäftsführer</p>
  </div>
  <div class="divider"></div>

  <div class="address">
    <svg class="icon icon--solid" viewBox="0 0 24 24" aria-hidden="true"><path d="M12 2a7 7 0 0 0-7 7c0 5.2 7 13 7 13s7-7.8 7-13a7 7 0 0 0-7-7zm0 9.5A2.5 2.5 0 1 1 12 6.5a2.5 2.5 0 0 1 0 5z"/></svg>
    <p>Am Lindenhang 12<br>34512 Wiesfeld</p>
  </div>

  <ul class="contact">
    <li>05642 / 71 38 20
      <svg class="icon" viewBox="0 0 24 24" aria-hidden="true"><path d="M6 3l3 4-2 2c1 2.5 3.5 5 6 6l2-2 4 3-2 4C10 20 4 14 3 6z"/></svg>
    </li>
    <li>05642 / 71 38 29
      <svg class="icon" viewBox="0 0 24 24" aria-hidden="true"><rect x="6" y="3" width="12" height="6"/><rect x="3" y="9" width="18" height="8" rx="1"/><rect x="7" y="14" width="10" height="7"/></svg>
    </li>
    <li>info@karmu-wiesfeld.de
      <svg class="icon" viewBox="0 0 24 24" aria-hidden="true"><rect x="3" y="5" width="18" height="14"/><path d="M3 5l9 8 9-8"/></svg>
    </li>
  </ul>
</section>

</body>
</html>
```